Long Established Local Fencing (not swords) Business needs fresh Business Cards

We need fresh double sided business cards for our Fencing Construction business, we are looking for something with our new logo design added, and maybe a photo background ?
We recently had cards made from Cardlyne and we were horrified with what we got back, the quality was terrible, so am looking for high quality format for good printing company to make.
We install Steelmora, Timber paling, Aluminium Slat Screening, Picket (timber and aluminium) and most other fencing installations.
Our website is brankelrails.com.au should you like to learn a bit more.
We do have logo in other formats if required.
We have been in business for over 35 years and we have used this as a "motto" it is on our signage

Industry/Entity Type

Construction

Contact Information for Business Card

Open to ideas, we need 3 x different cards, one generic with no name and 2 x others each with 1 of our bosses name on each, I will put into upload files.

Colors
ec1f27
000000
606060
f5f5f5

Requirements
Must have
• Company Name and Logo
• Address
• Contact details, phone, website, email etc
• Small space to write notes when leaving card at residence
Nice to have
• Our motto "Servicing the Peninsula for over 35 years"

```html
<!DOCTYPE html>
<html lang="en">
<head>
<meta charset="utf-8">
<title>Brankel Rails – Business Card</title>
<link rel="stylesheet" href="https://fonts.googleapis.com/css2?family=Open+Sans:wght@400;600&family=Oswald:wght@500&family=Fondamento&family=Archivo+Black&display=swap">
<style>
  :root{
    --red:#ec1f27;
    --black:#000000;
    --grey:#606060;
    --paper:#f5f5f5;
    --white:#ffffff;
    --bronze:#6b2a14;
  }
  html,body{margin:0;padding:0;overflow:hidden;background:var(--white);}
  .canvas{position:relative;width:988px;height:1200px;overflow:hidden;background:var(--white);font-family:"Open Sans",sans-serif;color:var(--black);}
  .card{position:absolute;left:0;width:988px;height:566px;overflow:hidden;background:var(--white);}
  .card--front{top:0;}
  .card--back{top:634px;}
  .card-art{position:absolute;inset:0;}
  .photo{position:absolute;}
  .brand{position:absolute;display:flex;align-items:center;gap:10px;font-family:"Archivo Black",sans-serif;color:var(--black);letter-spacing:1px;white-space:nowrap;}
  .brand-mark{background:var(--red);}
  .abn{position:absolute;right:37px;top:228px;font-size:14px;}
  .person{position:absolute;left:487px;top:246px;font-family:"Oswald",sans-serif;font-size:38px;line-height:1;}
  .licence{position:absolute;left:487px;top:294px;font-family:"Oswald",sans-serif;font-weight:500;font-size:18px;transform:scaleX(.85);transform-origin:left;color:#222;}
  .rule{position:absolute;left:486px;top:325px;width:467px;height:4px;background:var(--red);}
  .address{position:absolute;left:487px;top:334px;font-size:26px;}
  .contacts{position:absolute;left:489px;top:378px;margin:0;padding:0;list-style:none;}
  .contacts li{display:flex;align-items:center;height:39.5px;font-size:27px;}
  .contacts .icon{width:32px;height:32px;background:var(--red);margin-right:12px;display:flex;align-items:center;justify-content:center;}
  .card-label{position:absolute;left:0;width:988px;top:578px;text-align:center;font-size:40px;line-height:1.1;}
  .motto{position:absolute;right:37px;top:42px;text-align:right;font-family:"Fondamento",cursive;line-height:1;}
  .motto-line1{font-size:42px;color:var(--black);}
  .motto-line2{font-size:46px;color:var(--red);margin-top:-2px;}
  .notes{position:absolute;left:484px;top:288px;width:462px;}
  .notes span{display:block;height:54px;border-bottom:2.5px dotted #222;}
  .back-url{position:absolute;left:40px;top:486px;font-size:29px;}
</style>
</head>
<body>
<div class="canvas">

  <section class="card card--front">
    <svg class="card-art" width="988" height="566" viewBox="0 0 988 566">
      <defs>
        <linearGradient id="silver" x1="0" x2="1">
          <stop offset="0" stop-color="#8c8c8e"/><stop offset=".3" stop-color="#e8e8ea"/>
          <stop offset=".6" stop-color="#9a9a9c"/><stop offset="1" stop-color="#f0f0f2"/>
        </linearGradient>
        <linearGradient id="bronze" x1="0" x2="1">
          <stop offset="0" stop-color="#f2e3d5"/><stop offset=".5" stop-color="#b5794e"/><stop offset="1" stop-color="#4d1a0a"/>
        </linearGradient>
      </defs>
      <path d="M0 0H468Q400 283 466 566H0Z" fill="url(#bronze)"/>
      <path d="M0 0H448Q382 283 446 566H0Z" fill="url(#silver)"/>
    </svg>
    <div class="photo" role="img" aria-label="Photo of a corrugated steel garage and fence" style="left:38px;top:36px;width:218px;height:114px;background:linear-gradient(#b9c7a8,#8a8f86);"></div>
    <div class="photo" role="img" aria-label="Photo of a driveway with black steel railing fence" style="left:258px;top:36px;width:176px;height:114px;background:linear-gradient(#9dbb7d,#6f7d62);"></div>
    <div class="photo" role="img" aria-label="Photo of a long green steel fence with lattice top" style="left:38px;top:152px;width:368px;height:244px;background:linear-gradient(110deg,#a9b9a0,#7c9b6e 55%,#c7cfb0);"></div>
    <div class="photo" role="img" aria-label="Photo of a black aluminium gate and hedge" style="left:38px;top:398px;width:198px;height:130px;background:linear-gradient(#aa7a5c,#4f6a3a);"></div>
    <div class="photo" role="img" aria-label="Photo of a blue steel fence in front of a house" style="left:238px;top:398px;width:170px;height:130px;background:linear-gradient(#6c86b8,#24408c);"></div>

    <div class="brand" style="right:37px;top:166px;font-size:40px;">
      <span class="brand-mark" style="width:26px;height:26px;"></span>BRANKEL RAILS
    </div>
    <div class="abn">ABN 41 852 06 319</div>
    <div class="person">Tom Harlen</div>
    <div class="licence">Gold License No: 52617K</div>
    <div class="rule"></div>
    <div class="address"># Po Box 218, Kelmore NSW 2261.</div>
    <ul class="contacts">
      <li><span class="icon"><svg width="18" height="18" viewBox="0 0 24 24"><path d="M6 2l4 4-2 3q2 4 7 7l3-2 4 4-3 3Q8 20 3 5z" fill="#fff"/></svg></span>(02)4 390 2718</li>
      <li><span class="icon"><svg width="14" height="20" viewBox="0 0 14 20"><rect x="1" y="1" width="12" height="18" rx="2" fill="#fff"/><rect x="3" y="3" width="8" height="11" fill="#ec1f27"/></svg></span>0418 275 903</li>
      <li><span class="icon"><svg width="20" height="14" viewBox="0 0 20 14"><rect x="1" y="1" width="18" height="12" fill="none" stroke="#fff" stroke-width="2"/><path d="M1 1l9 7 9-7M1 13l7-6M19 13l-7-6" fill="none" stroke="#fff" stroke-width="1.6"/></svg></span>office@brankelrails.com.au</li>
      <li><span class="icon"><svg width="20" height="20" viewBox="0 0 20 20" fill="none" stroke="#fff" stroke-width="1.6"><circle cx="10" cy="10" r="8"/><ellipse cx="10" cy="10" rx="3.5" ry="8"/><path d="M2 10h16M3.5 6h13M3.5 14h13"/></svg></span>www.brankelrails.com.au</li>
    </ul>
  </section>

  <div class="card-label">Tom Harlen Card</div>

  <section class="card card--back">
    <div class="photo" role="img" aria-label="Faded photo of a cream steel fence along a driveway" style="left:0;top:0;width:988px;height:566px;background:linear-gradient(180deg,#f7f8f8,#e4e7e6 60%,#d9dcda);"></div>
    <svg class="card-art" width="988" height="566" viewBox="0 0 988 566">
      <defs>
        <linearGradient id="silver2" x1="0" x2="1">
          <stop offset="0" stop-color="#8e8e90"/><stop offset=".3" stop-color="#efeff1"/>
          <stop offset=".62" stop-color="#8f8f91"/><stop offset="1" stop-color="#f2f2f4"/>
        </linearGradient>
      </defs>
      <path d="M0 0H510Q400 283 470 566H0Z" fill="url(#silver2)"/>
    </svg>
    <div class="motto">
      <div class="motto-line1">Servicing the Peninsula</div>
      <div class="motto-line2">for over 30 years</div>
    </div>
    <div class="notes"><span></span><span></span><span></span><span></span><span></span></div>
    <div class="brand" style="left:44px;top:320px;font-size:38px;">
      <span class="brand-mark" style="width:26px;height:26px;"></span>BRANKEL RAILS
    </div>
    <div class="back-url">www.brankelrails.com.au</div>
  </section>

</div>
</body>
</html>
```